Country Infographic Design template

We need a skilled graphic designer to continue working on our website. Currently, we are looking to create Infographic Pages for each country/city we visit/travel to. Currently, we are looking for Vietnam, the United Kingdom, Switzerland, South Africa, and Qatar. A Sample of Egypt and Jamaica is attached.
In a SIMILAR design format and style, we would need the following:
* MAP for Vietnam, the United Kingdom, Switzerland, South Africa, and Qatar.
* Country-specific Icons for the "Top Experiences" Section (i.e Pandas, Temples, Museums.
* Flag of the country

Later we will need caricature modifications/updates as well.

We would like to see a replica adaptation to the example attached based on the look and feel of the page we provided to you.

Formats in Illustrator or Photoshop preferred (full layers should be provided to modify aspects of the infographic.

Requirements
Must have
• Ability to design maps and icons as shown in a similar manner as the examples.

```html
<!DOCTYPE html>
<html lang="en">
<head>
<meta charset="utf-8">
<title>Vietnam – Infographic Travel Guide</title>
<link rel="stylesheet" href="https://fonts.googleapis.com/css2?family=Bowlby+One&family=Roboto+Condensed:wght@400;500;700&family=Roboto:wght@400;500&display=swap">
<style>
:root{
  --navy:#1f2a6b;
  --orange:#ef9a2c;
  --orange-dark:#d9801f;
  --orange-soft:#eeb24f;
  --sky:#b9dff5;
  --card:#d2ebfb;
  --blue:#1b6fb5;
  --ink:#26313d;
  --white:#ffffff;
  --grey:#7b8794;
  --grey-light:#d9dee5;
  --red:#e2483d;
  --green:#4e9a4a;
  --yellow:#f7c52b;
  --sand:#e9c27a;
  --sea:#3f8fe0;
  --flag-red:#d8262c;
  --flag-star:#f7d417;
}
*{box-sizing:border-box;margin:0;padding:0}
html,body{width:1200px;height:5357px;overflow:hidden;background:var(--white)}
body{position:relative;font-family:"Roboto",Arial,sans-serif;color:var(--ink)}
.abs{position:absolute}
.display{font-family:"Bowlby One",Impact,sans-serif;letter-spacing:1px}

/* header */
.brand{left:70px;top:100px;display:flex;align-items:center;gap:12px}
.brand-dot{width:26px;height:26px;border-radius:50%;background:var(--orange)}
.brand-name{font-family:"Roboto Condensed",sans-serif;font-weight:700;font-size:34px;color:var(--navy)}
.title{left:300px;width:600px;top:40px;text-align:center;font-size:82px;color:var(--navy);line-height:1}
.ribbon{left:275px;top:138px;width:650px;height:70px}
.ribbon-text{left:275px;top:148px;width:650px;text-align:center;font-size:28px;color:var(--white);line-height:40px}
.flag{left:950px;top:60px;width:206px;height:140px}
.map{left:115px;top:265px;width:970px;height:480px}

.fact-icon{display:block}
.fact-label{font-family:"Roboto Condensed",sans-serif;font-size:22px;color:var(--orange);line-height:26px}
.fact-value{font-family:"Roboto Condensed",sans-serif;font-weight:700;font-size:40px;line-height:52px;color:var(--orange)}

/* information */
.info{left:0;top:1323px;width:1200px;height:1055px;background:var(--orange-soft)}
.info-frame{left:48px;top:42px;width:1104px;height:970px;border:4px dashed var(--white);border-radius:14px}
.section-title{width:1200px;left:0;text-align:center;color:var(--white);font-size:62px;line-height:1}
.info-item{width:360px;text-align:center;color:var(--white)}
.info-icon{display:block;width:170px;height:170px;margin:0 auto 24px}
.info-head{font-family:"Roboto Condensed",sans-serif;font-weight:700;font-size:40px;line-height:46px}
.info-text{font-size:18px;line-height:25px;margin:6px auto 0;width:310px}

/* experiences */
.exp{left:0;top:2378px;width:1200px;height:1694px;background:var(--sky)}
.card{width:334px;height:376px;background:var(--card);border-radius:14px;text-align:center;padding-top:30px}
.card-icon{display:block;width:160px;height:140px;margin:0 auto 20px}
.card-head{font-family:"Roboto Condensed",sans-serif;font-weight:700;font-size:34px;line-height:43px;color:var(--blue)}
.card-text{font-size:16px;line-height:21px;width:280px;margin:8px auto 0;color:var(--ink)}

/* tips */
.tips-title{left:0;top:4160px;width:1200px;text-align:center;font-size:62px;color:var(--orange-soft);line-height:1}
.tip{width:478px}
.tip-head{font-family:"Roboto Condensed",sans-serif;font-weight:700;font-size:34px;color:var(--blue);line-height:40px;margin-bottom:4px}
.tip-text{font-size:16px;line-height:21.5px;color:var(--ink)}

/* footer */
.footer{left:0;top:5098px;width:1200px;height:259px;background:var(--orange-soft)}
.footer-brand{left:34px;top:110px;display:flex;align-items:center;gap:10px}
.footer-brand .brand-name{color:var(--white);font-size:32px}
.footer-brand .brand-dot{background:var(--white)}
.divider{top:30px;height:200px;border-left:4px dotted var(--white)}
.footer-copy{left:220px;top:76px;width:580px;text-align:center;color:var(--white);font-size:28px;line-height:37px}
.footer-url{left:220px;top:166px;width:580px;text-align:center;color:var(--white);font-family:"Roboto Condensed",sans-serif;font-weight:500;font-size:34px}
.socials{left:845px;top:68px;list-style:none}
.socials li{display:flex;align-items:center;gap:16px;color:var(--white);font-size:28px;line-height:36px}
.socials li::before{content:"";width:18px;height:18px;border-radius:50%;background:var(--white)}
</style>
</head>
<body>

<header>
  <div class="abs brand"><span class="brand-dot"></span><span class="brand-name">Roam Pals</span></div>
  <h1 class="abs title display">VIETNAM</h1>
  <svg class="abs ribbon" viewBox="0 0 650 70" aria-hidden="true">
    <polygon points="0,18 70,18 70,66 0,66 18,42" fill="var(--orange-dark)"/>
    <polygon points="650,18 580,18 580,66 650,66 632,42" fill="var(--orange-dark)"/>
    <rect x="45" y="4" width="560" height="50" fill="var(--orange)"/>
    <polygon points="45,54 70,54 70,66" fill="#a85c12"/>
    <polygon points="605,54 580,54 580,66" fill="#a85c12"/>
  </svg>
  <div class="abs ribbon-text display">INFOGRAPHIC TRAVEL GUIDE</div>
  <svg class="abs flag" viewBox="0 0 206 140" role="img" aria-label="Flag of Vietnam">
    <rect width="206" height="140" fill="var(--flag-red)"/>
    <polygon points="103,28 113,59 146,59 119,78 129,110 103,90 77,110 87,78 60,59 93,59" fill="var(--flag-star)"/>
  </svg>
</header>

<svg class="abs map" viewBox="0 0 970 480" role="img" aria-label="Illustrated map of Vietnam on a blue sea with landmarks, boats and planes">
  <defs>
    <radialGradient id="mapTone" cx="55%" cy="45%" r="60%">
      <stop offset="0" stop-color="#8fbf55"/>
      <stop offset="0.22" stop-color="#5ea3a0"/>
      <stop offset="0.5" stop-color="#3f8fe0"/>
      <stop offset="0.85" stop-color="#7ab6f0"/>
      <stop offset="1" stop-color="#cfe4fb"/>
    </radialGradient>
  </defs>
  <path d="M40,250 C20,130 220,30 470,40 C720,30 955,110 945,250 C935,390 710,470 475,465 C230,470 60,380 40,250Z" fill="url(#mapTone)"/>
</svg>

<section class="facts">
  <svg class="abs fact-icon" style="left:94px;top:740px;width:92px;height:92px" viewBox="0 0 100 100" aria-hidden="true">
    <polygon points="50,8 94,30 6,30" fill="#8a95a5"/>
    <rect x="10" y="30" width="80" height="8" fill="#6b7685"/>
    <rect x="17" y="42" width="9" height="38" fill="var(--grey-light)"/>
    <rect x="33" y="42" width="9" height="38" fill="var(--grey-light)"/>
    <rect x="58" y="42" width="9" height="38" fill="var(--grey-light)"/>
    <rect x="74" y="42" width="9" height="38" fill="var(--grey-light)"/>
    <rect x="45" y="54" width="10" height="26" fill="var(--red)"/>
    <rect x="6" y="82" width="88" height="10" fill="#6b7685"/>
  </svg>
  <div class="abs" style="left:212px;top:746px"><div class="fact-label">Capital:</div><div class="fact-value">HANOI</div></div>

  <svg class="abs fact-icon" style="left:78px;top:866px;width:120px;height:64px" viewBox="0 0 120 64" aria-hidden="true">
    <circle cx="20" cy="14" r="10" fill="var(--orange)"/><rect x="8" y="27" width="24" height="35" rx="6" fill="var(--orange)"/>
    <circle cx="60" cy="14" r="10" fill="var(--orange-dark)"/><rect x="48" y="27" width="24" height="35" rx="6" fill="var(--orange-dark)"/>
    <circle cx="100" cy="14" r="10" fill="var(--orange)"/><rect x="88" y="27" width="24" height="35" rx="6" fill="var(--orange)"/>
  </svg>
  <div class="abs" style="left:212px;top:862px"><div class="fact-label">Population:</div><div class="fact-value">97.47 million )2021 est)</div></div>

  <svg class="abs fact-icon" style="left:80px;top:992px;width:116px;height:110px" viewBox="0 0 116 110" aria-hidden="true">
    <ellipse cx="58" cy="92" rx="56" ry="14" fill="var(--sea)"/>
    <ellipse cx="58" cy="86" rx="36" ry="12" fill="var(--sand)"/>
    <path d="M62,84 C60,60 66,40 72,26" stroke="#8a5a2b" stroke-width="6" fill="none"/>
    <ellipse cx="60" cy="26" rx="18" ry="7" fill="var(--green)" transform="rotate(-20 60 26)"/>
    <ellipse cx="86" cy="26" rx="18" ry="7" fill="var(--green)" transform="rotate(25 86 26)"/>
    <ellipse cx="74" cy="16" rx="7" ry="16" fill="#3d8a3a"/>
    <circle cx="22" cy="22" r="12" fill="var(--yellow)"/>
  </svg>
  <div class="abs" style="left:212px;top:978px"><div class="fact-label">Area :</div><div class="fact-value">127,882 sq mi<br>(331,212 km2 km)</div></div>

  <svg class="abs fact-icon" style="left:94px;top:1138px;width:92px;height:92px" viewBox="0 0 100 100" aria-hidden="true">
    <polygon points="50,8 94,30 6,30" fill="#8a95a5"/>
    <rect x="10" y="30" width="80" height="8" fill="#6b7685"/>
    <rect x="17" y="42" width="9" height="38" fill="var(--grey-light)"/>
    <rect x="33" y="42" width="9" height="38" fill="var(--grey-light)"/>
    <rect x="58" y="42" width="9" height="38" fill="var(--grey-light)"/>
    <rect x="74" y="42" width="9" height="38" fill="var(--grey-light)"/>
    <rect x="45" y="42" width="10" height="38" fill="var(--grey-light)"/>
    <rect x="6" y="82" width="88" height="10" fill="#6b7685"/>
  </svg>
  <div class="abs" style="left:212px;top:1148px"><div class="fact-label">Government:</div><div class="fact-value">The National Assembly</div></div>

  <svg class="abs fact-icon" style="left:738px;top:857px;width:58px;height:96px" viewBox="0 0 58 96" aria-hidden="true">
    <rect x="2" y="2" width="54" height="92" rx="8" fill="#2d3a4f"/>
    <rect x="8" y="14" width="42" height="64" rx="3" fill="#3b7fd6"/>
    <text x="29" y="58" text-anchor="middle" font-family="Roboto Condensed, sans-serif" font-weight="700" font-size="28" fill="#ffffff">#</text>
    <circle cx="29" cy="86" r="4" fill="#5a6780"/>
  </svg>
  <div class="abs" style="left:832px;top:862px"><div class="fact-label">Country code:</div><div class="fact-value">+84</div></div>

  <svg class="abs fact-icon" style="left:718px;top:994px;width:98px;height:96px" viewBox="0 0 100 100" aria-hidden="true">
    <rect x="14" y="76" width="18" height="18" rx="4" fill="#9aa4b0"/>
    <rect x="68" y="76" width="18" height="18" rx="4" fill="#9aa4b0"/>
    <circle cx="50" cy="50" r="44" fill="#9aa4b0"/>
    <circle cx="50" cy="50" r="36" fill="var(--white)"/>
    <g fill="var(--red)"><rect x="48" y="18" width="4" height="8"/><rect x="48" y="74" width="4" height="8"/><rect x="18" y="48" width="8" height="4"/><rect x="74" y="48" width="8" height="4"/></g>
    <line x1="50" y1="50" x2="50" y2="28" stroke="#2d3a4f" stroke-width="5" stroke-linecap="round"/>
    <line x1="50" y1="50" x2="66" y2="58" stroke="#2d3a4f" stroke-width="5" stroke-linecap="round"/>
    <circle cx="50" cy="50" r="4" fill="var(--red)"/>
  </svg>
  <div class="abs" style="left:800px;top:978px"><div class="fact-label">Timezone:</div><div class="fact-value">Indochina Time<br>(GMT+7)</div></div>

  <svg class="abs fact-icon" style="left:718px;top:1134px;width:98px;height:98px" viewBox="0 0 100 100" aria-hidden="true">
    <g fill="var(--orange)">
      <polygon points="50,0 58,18 42,18"/><polygon points="50,100 58,82 42,82"/>
      <polygon points="0,50 18,42 18,58"/><polygon points="100,50 82,42 82,58"/>
      <polygon points="15,15 32,22 22,32"/><polygon points="85,15 78,32 68,22"/>
      <polygon points="15,85 22,68 32,78"/><polygon points="85,85 68,78 78,68"/>
    </g>
    <circle cx="50" cy="50" r="32" fill="var(--yellow)"/>
  </svg>
  <div class="abs" style="left:832px;top:1148px"><div class="fact-label">Climate ( diverse due to size):</div><div class="fact-value">Tropical</div></div>
</section>

<section class="abs info">
  <div class="abs info-frame"></div>
  <h2 class="abs section-title display" style="top:105px">INFORMATION</h2>

  <div class="abs info-item" style="left:56px;top:236px">
    <svg class="info-icon" viewBox="0 0 100 100" aria-hidden="true">
      <rect x="8" y="50" width="20" height="40" rx="4" fill="var(--white)" stroke="#2d3a4f" stroke-width="2.5"/>
      <rect x="12" y="42" width="12" height="9" fill="#2d3a4f"/>
      <rect x="8" y="62" width="20" height="12" fill="#58a6e8"/>
      <rect x="32" y="56" width="18" height="34" rx="4" fill="var(--white)" stroke="#2d3a4f" stroke-width="2.5"/>
      <rect x="36" y="49" width="10" height="8" fill="#2d3a4f"/>
      <rect x="32" y="66" width="18" height="10" fill="#58a6e8"/>
      <g transform="rotate(-45 66 44)">
        <rect x="58" y="18" width="16" height="46" rx="3" fill="var(--white)" stroke="#2d3a4f" stroke-width="2.5"/>
        <rect x="58" y="36" width="16" height="28" fill="var(--yellow)" opacity=".8"/>
        <rect x="63" y="6" width="6" height="12" fill="#2d3a4f"/>
        <rect x="55" y="2" width="22" height="5" rx="2" fill="#2d3a4f"/>
        <line x1="66" y1="64" x2="66" y2="84" stroke="#2d3a4f" stroke-width="2.5"/>
      </g>
    </svg>
    <div class="info-head">VACCINATION</div>
    <p class="info-text">See a travel clinic about six weeks before you fly and keep your records handy.</p>
  </div>
  <div class="abs info-item" style="left:420px;top:236px">
    <svg class="info-icon" viewBox="0 0 100 100" aria-hidden="true">
      <g transform="rotate(12 70 46)">
        <rect x="50" y="10" width="34" height="72" rx="4" fill="#f4f4f4" stroke="#2d3a4f" stroke-width="2.5"/>
        <line x1="56" y1="62" x2="78" y2="62" stroke="#2d3a4f" stroke-width="2" stroke-dasharray="3 3"/>
        <line x1="58" y1="70" x2="76" y2="70" stroke="#2d3a4f" stroke-width="3"/>
      </g>
      <rect x="14" y="16" width="52" height="74" rx="5" fill="#2b3f8f" stroke="#1c2b66" stroke-width="2.5"/>
      <circle cx="40" cy="46" r="15" fill="none" stroke="var(--yellow)" stroke-width="3"/>
      <ellipse cx="40" cy="46" rx="6" ry="15" fill="none" stroke="var(--yellow)" stroke-width="2.5"/>
      <line x1="25" y1="46" x2="55" y2="46" stroke="var(--yellow)" stroke-width="2.5"/>
      <rect x="28" y="72" width="24" height="4" fill="var(--yellow)"/>
    </svg>
    <div class="info-head">TRAVEL DOCS</div>
    <p class="info-text">Your passport should stay valid for six months; print the e-visa approval too.</p>
  </div>
  <div class="abs info-item" style="left:783px;top:236px">
    <svg class="info-icon" viewBox="0 0 100 100" aria-hidden="true">
      <rect x="6" y="10" width="48" height="32" rx="8" fill="#7cc27a" stroke="#2d3a4f" stroke-width="2.5"/>
      <polygon points="14,42 24,42 12,54" fill="#7cc27a" stroke="#2d3a4f" stroke-width="2.5" stroke-linejoin="round"/>
      <line x1="16" y1="22" x2="44" y2="22" stroke="#2d3a4f" stroke-width="3"/>
      <line x1="16" y1="31" x2="36" y2="31" stroke="#2d3a4f" stroke-width="3"/>
      <rect x="44" y="52" width="50" height="32" rx="8" fill="var(--yellow)" stroke="#2d3a4f" stroke-width="2.5"/>
      <polygon points="86,84 76,84 88,96" fill="var(--yellow)" stroke="#2d3a4f" stroke-width="2.5" stroke-linejoin="round"/>
      <line x1="54" y1="64" x2="84" y2="64" stroke="#2d3a4f" stroke-width="3"/>
      <line x1="54" y1="73" x2="76" y2="73" stroke="#2d3a4f" stroke-width="3"/>
    </svg>
    <div class="info-head">LANGUAGE</div>
    <p class="info-text">Learn a few polite phrases; people warmly welcome any effort you make to speak.</p>
  </div>
  <div class="abs info-item" style="left:56px;top:616px">
    <svg class="info-icon" viewBox="0 0 100 100" aria-hidden="true">
      <rect x="6" y="14" width="60" height="40" rx="4" fill="#6bb36a" stroke="#2d3a4f" stroke-width="2.5" transform="rotate(-10 36 34)"/>
      <rect x="12" y="26" width="60" height="40" rx="4" fill="#84c983" stroke="#2d3a4f" stroke-width="2.5"/>
      <circle cx="42" cy="46" r="10" fill="none" stroke="#2d3a4f" stroke-width="2.5"/>
      <ellipse cx="70" cy="86" rx="22" ry="8" fill="#e5a92a" stroke="#2d3a4f" stroke-width="2.5"/>
      <ellipse cx="70" cy="78" rx="22" ry="8" fill="var(--yellow)" stroke="#2d3a4f" stroke-width="2.5"/>
      <circle cx="72" cy="60" r="18" fill="var(--yellow)" stroke="#2d3a4f" stroke-width="2.5"/>
      <text x="72" y="68" text-anchor="middle" font-family="Roboto Condensed, sans-serif" font-weight="700" font-size="22" fill="#2d3a4f">$</text>
    </svg>
    <div class="info-head">CURRENCY</div>
    <p class="info-text">Carry some cash in dong for markets, street food stalls and short taxi rides.</p>
  </div>
  <div class="abs info-item" style="left:420px;top:616px">
    <svg class="info-icon" viewBox="0 0 100 100" aria-hidden="true">
      <circle cx="44" cy="54" r="38" fill="var(--red)" stroke="#2d3a4f" stroke-width="2.5"/>
      <circle cx="44" cy="54" r="28" fill="#dff0fb" stroke="#2d3a4f" stroke-width="2.5"/>
      <line x1="44" y1="54" x2="44" y2="34" stroke="#2d3a4f" stroke-width="4" stroke-linecap="round"/>
      <line x1="44" y1="54" x2="58" y2="62" stroke="#2d3a4f" stroke-width="4" stroke-linecap="round"/>
      <circle cx="78" cy="22" r="16" fill="#6bb36a" stroke="#2d3a4f" stroke-width="2.5"/>
      <polyline points="70,22 76,28 87,16" fill="none" stroke="var(--white)" stroke-width="4" stroke-linecap="round" stroke-linejoin="round"/>
    </svg>
    <div class="info-head">BEST TIME TO VISIT</div>
    <p class="info-text">Spring and autumn bring mild, drier weather across the north, centre and south.</p>
  </div>
  <div class="abs info-item" style="left:783px;top:616px">
    <svg class="info-icon" viewBox="0 0 100 100" aria-hidden="true">
      <circle cx="44" cy="56" r="36" fill="var(--white)" stroke="var(--red)" stroke-width="8"/>
      <line x1="20" y1="32" x2="68" y2="80" stroke="var(--red)" stroke-width="8"/>
      <polygon points="74,6 96,44 52,44" fill="var(--yellow)" stroke="#2d3a4f" stroke-width="2.5" stroke-linejoin="round"/>
      <rect x="72" y="18" width="4" height="14" fill="#2d3a4f"/>
      <circle cx="74" cy="37" r="2.5" fill="#2d3a4f"/>
    </svg>
    <div class="info-head">$ RESTRICTIONS</div>
    <p class="info-text">Declare large sums of cash on arrival and check customs rules before packing.</p>
  </div>
</section>

<section class="abs exp">
  <h2 class="abs section-title display" style="top:115px">TOP EXPERIENCES</h2>

  <div class="abs card" style="left:57px;top:298px">
    <svg class="card-icon" viewBox="0 0 160 140" aria-hidden="true">
      <rect x="14" y="52" width="80" height="78" fill="#c6ccd4" stroke="#3a4350" stroke-width="3"/>
      <rect x="22" y="30" width="12" height="24" fill="#8f99a6" stroke="#3a4350" stroke-width="3"/>
      <rect x="84" y="38" width="60" height="92" fill="#e6e9ee" stroke="#3a4350" stroke-width="3"/>
      <rect x="96" y="20" width="12" height="20" fill="#8f99a6" stroke="#3a4350" stroke-width="3"/>
      <g fill="#3a4350">
        <rect x="24" y="70" width="6" height="16"/><rect x="38" y="70" width="6" height="16"/><rect x="52" y="70" width="6" height="16"/><rect x="66" y="70" width="6" height="16"/>
        <rect x="24" y="98" width="6" height="16"/><rect x="38" y="98" width="6" height="16"/><rect x="52" y="98" width="6" height="16"/><rect x="66" y="98" width="6" height="16"/>
        <rect x="98" y="56" width="6" height="16"/><rect x="122" y="56" width="6" height="16"/>
        <rect x="98" y="90" width="6" height="16"/><rect x="122" y="90" width="6" height="16"/>
      </g>
    </svg>
    <div class="card-head">Discover Hanoi<br>Old Quarter</div>
    <p class="card-text">Wander narrow lanes of craft shops, temples and busy corner cafes by the lake.</p>
  </div>
  <div class="abs card" style="left:433px;top:298px">
    <svg class="card-icon" viewBox="0 0 160 140" aria-hidden="true">
      <rect x="72" y="108" width="16" height="26" fill="#7a4a22"/>
      <polygon points="80,6 104,42 56,42" fill="#4f9a47"/>
      <polygon points="80,26 112,72 48,72" fill="#438a3d"/>
      <polygon points="80,54 120,110 40,110" fill="#3a7d35"/>
    </svg>
    <div class="card-head">Overnight stay with<br>Halong Bay Cruises</div>
    <p class="card-text">Sleep on deck among limestone islands rising straight from emerald water.</p>
  </div>
  <div class="abs card" style="left:809px;top:298px">
    <svg class="card-icon" viewBox="0 0 160 140" aria-hidden="true">
      <rect x="96" y="18" width="12" height="22" fill="#2d3a4f"/>
      <rect x="50" y="38" width="70" height="30" rx="4" fill="#f1f3f6"/>
      <rect x="60" y="46" width="10" height="10" fill="#58a6e8"/><rect x="78" y="46" width="10" height="10" fill="#58a6e8"/><rect x="96" y="46" width="10" height="10" fill="#58a6e8"/>
      <polygon points="10,68 150,68 136,100 22,100" fill="var(--red)"/>
      <rect x="22" y="80" width="120" height="5" fill="var(--white)"/>
      <path d="M0,102 Q20,94 40,102 T80,102 T120,102 T160,102 V140 H0Z" fill="#3b85d0"/>
    </svg>
    <div class="card-head">Stunning scenery<br>of Trang boat trip</div>
    <p class="card-text">Glide by rowing boat through caves, rice fields and quiet riverside pagodas.</p>
  </div>

  <div class="abs card" style="left:57px;top:744px">
    <svg class="card-icon" viewBox="0 0 160 140" aria-hidden="true">
      <g fill="#ea5a2b">
        <rect x="36" y="10" width="14" height="124"/>
        <rect x="110" y="10" width="14" height="124"/>
        <rect x="0" y="84" width="160" height="10"/>
        <rect x="36" y="30" width="88" height="6"/>
      </g>
      <path d="M0,60 Q22,84 43,20 Q80,100 117,20 Q138,84 160,60" fill="none" stroke="#ea5a2b" stroke-width="5"/>
      <g stroke="#ea5a2b" stroke-width="3">
        <line x1="60" y1="50" x2="60" y2="84"/><line x1="80" y1="60" x2="80" y2="84"/><line x1="100" y1="50" x2="100" y2="84"/>
        <line x1="18" y1="66" x2="18" y2="84"/><line x1="142" y1="66" x2="142" y2="84"/>
      </g>
    </svg>
    <div class="card-head">Visit the world<br>famous Golden Bridge</div>
    <p class="card-text">Walk the bridge held aloft by giant stone hands high above the misty forest.</p>
  </div>
  <div class="abs card" style="left:433px;top:744px">
    <svg class="card-icon" viewBox="0 0 160 140" aria-hidden="true">
      <rect x="72" y="48" width="62" height="56" fill="#f1f3f6" stroke="#3a4350" stroke-width="3"/>
      <polygon points="66,50 103,14 140,50" fill="#e65a4f" stroke="#3a4350" stroke-width="3" stroke-linejoin="round"/>
      <rect x="104" y="64" width="18" height="16" fill="#58a6e8" stroke="#3a4350" stroke-width="2.5"/>
      <rect x="20" y="82" width="60" height="52" fill="#f1f3f6" stroke="#3a4350" stroke-width="3"/>
      <polygon points="14,84 50,52 86,84" fill="#e65a4f" stroke="#3a4350" stroke-width="3" stroke-linejoin="round"/>
      <rect x="30" y="100" width="16" height="34" fill="#f0a54a" stroke="#3a4350" stroke-width="2.5"/>
      <rect x="56" y="98" width="16" height="14" fill="#58a6e8" stroke="#3a4350" stroke-width="2.5"/>
    </svg>
    <div class="card-head">Enchanting Hoi<br>An Ancient Town</div>
    <p class="card-text">Stroll lantern-lit lanes, tailor shops and riverside markets after the sunset.</p>
  </div>
  <div class="abs card" style="left:809px;top:744px">
    <svg class="card-icon" viewBox="0 0 160 140" aria-hidden="true">
      <ellipse cx="82" cy="114" rx="76" ry="20" fill="var(--sand)"/>
      <g fill="#d9a85c">
        <rect x="86" y="52" width="56" height="56"/>
        <rect x="100" y="28" width="28" height="26"/>
        <rect x="86" y="44" width="10" height="10"/><rect x="106" y="44" width="10" height="10"/><rect x="132" y="44" width="10" height="10"/>
        <rect x="100" y="20" width="8" height="8"/><rect x="120" y="20" width="8" height="8"/>
      </g>
      <rect x="108" y="84" width="12" height="24" fill="#b9843f"/>
      <polygon points="18,62 72,62 64,110 26,110" fill="var(--red)"/>
      <rect x="14" y="56" width="62" height="10" rx="3" fill="#c93a30"/>
      <rect x="38" y="76" width="14" height="14" fill="var(--yellow)"/>
    </svg>
    <div class="card-head">Sun-sand-sea<br>activities at beaches</div>
    <p class="card-text">Swim, paddle and dive along the long white sandy beaches of the central coast.</p>
  </div>

  <div class="abs card" style="left:57px;top:1190px">
    <svg class="card-icon" viewBox="0 0 160 140" aria-hidden="true">
      <rect x="30" y="60" width="34" height="74" fill="#8f99a6" stroke="#3a4350" stroke-width="3"/>
      <rect x="62" y="18" width="44" height="116" fill="#c6ccd4" stroke="#3a4350" stroke-width="3"/>
      <rect x="104" y="48" width="30" height="86" fill="#8f99a6" stroke="#3a4350" stroke-width="3"/>
      <g fill="#3a4350">
        <rect x="70" y="28" width="8" height="8"/><rect x="90" y="28" width="8" height="8"/>
        <rect x="70" y="46" width="8" height="8"/><rect x="90" y="46" width="8" height="8"/>
        <rect x="70" y="64" width="8" height="8"/><rect x="90" y="64" width="8" height="8"/>
        <rect x="70" y="82" width="8" height="8"/><rect x="90" y="82" width="8" height="8"/>
        <rect x="70" y="100" width="8" height="8"/><rect x="90" y="100" width="8" height="8"/>
        <rect x="38" y="72" width="6" height="8"/><rect x="50" y="72" width="6" height="8"/>
        <rect x="38" y="92" width="6" height="8"/><rect x="50" y="92" width="6" height="8"/>
        <rect x="112" y="60" width="6" height="8"/><rect x="122" y="60" width="6" height="8"/>
        <rect x="112" y="82" width="6" height="8"/><rect x="122" y="82" width="6" height="8"/>
      </g>
    </svg>
    <div class="card-head">Embrace the<br>Ho Chi Minh City</div>
    <p class="card-text">Ride through busy boulevards, colonial halls and buzzing night food streets.</p>
  </div>
  <div class="abs card" style="left:433px;top:1190px">
    <svg class="card-icon" viewBox="0 0 160 140" aria-hidden="true">
      <polygon points="84,6 84,100 40,100" fill="#4f9a47"/>
      <line x1="86" y1="4" x2="86" y2="108" stroke="#3a4350" stroke-width="4"/>
      <ellipse cx="86" cy="110" rx="52" ry="7" fill="#2d3a4f"/>
      <path d="M10,122 Q40,110 80,124 T150,120" fill="none" stroke="#3b85d0" stroke-width="6" stroke-linecap="round"/>
    </svg>
    <div class="card-head">Make an authentic<br>cultural journey</div>
    <p class="card-text">Meet village artisans, share a family meal and learn old local customs.</p>
  </div>
  <div class="abs card" style="left:809px;top:1190px">
    <svg class="card-icon" viewBox="0 0 160 140" aria-hidden="true">
      <g fill="#f3a21f">
        <polygon points="80,2 88,24 72,24"/><polygon points="80,138 88,116 72,116"/>
        <polygon points="10,70 32,62 32,78"/><polygon points="150,70 128,62 128,78"/>
        <polygon points="30,20 48,32 40,40"/><polygon points="130,20 120,40 112,32"/>
        <polygon points="30,120 40,100 48,108"/><polygon points="130,120 112,108 120,100"/>
      </g>
      <circle cx="80" cy="70" r="40" fill="var(--yellow)"/>
    </svg>
    <div class="card-head">Witness sunset in<br>Phu Quoc island</div>
    <p class="card-text">Watch the sky turn gold over a calm sea from a quiet west coast beach.</p>
  </div>
</section>

<section class="tips">
  <h2 class="abs tips-title display">RP 5 TRAVEL TIPS</h2>

  <div class="abs tip" style="left:103px;top:4292px">
    <h3 class="tip-head">WHAT TO PACK</h3>
    <p class="tip-text">Bring light cotton clothes, a rain jacket and sturdy sandals for wet streets. Pack a scarf or long trousers for temple visits, plus sunscreen, insect repellent and a small first aid kit. A universal adapter, a reusable bottle and a light daypack make long days of walking, boat trips and markets far easier.</p>
  </div>
  <div class="abs tip" style="left:103px;top:4614px">
    <h3 class="tip-head">LOCAL FOOD TO TRY</h3>
    <p class="tip-text">Start the day with a steaming bowl of pho and strong drip coffee with condensed milk. Try banh mi from a street cart, fresh spring rolls and bun cha grilled over charcoal in Hanoi. In Hoi An look for cao lau noodles, and down south sample broken rice and tropical fruit from floating markets.</p>
  </div>
  <div class="abs tip" style="left:103px;top:4812px">
    <h3 class="tip-head">PHONE &amp; WIFI</h3>
    <p class="tip-text">A local SIM card with plenty of data costs little and is sold in every airport arrival hall; bring your passport to register it. Free wifi is common in hotels, cafes and restaurants, though speeds vary in rural areas. Download offline maps and a translation app before heading into the hills.</p>
  </div>
  <div class="abs tip" style="left:646px;top:4292px">
    <h3 class="tip-head">TRANSPORTATION</h3>
    <p class="tip-text">Domestic flights link Hanoi, Da Nang and Ho Chi Minh City in about an hour and are often cheaper than you expect. The overnight train along the coast is slower but gives wonderful views of rice fields and sea. In cities, use ride hailing apps for motorbikes and cars so the price is fixed before you set off. Sleeper buses reach most towns at low cost, yet the berths are short for tall travellers. Book long routes a few days ahead in the holiday season. If you rent a scooter, wear a helmet, carry a valid licence and take extra care at busy crossings and in heavy rain. Keep small notes for tolls, parking and drivers.</p>
  </div>
  <div class="abs tip" style="left:646px;top:4812px">
    <h3 class="tip-head">TO TIP OR NOT TO BE</h3>
    <p class="tip-text">Tipping is not expected but always appreciated. Round up taxi fares, leave small change at cafes, and give a little extra to guides and boat crews who look after you well. Some upscale hotels add a service charge, so check the bill first, and hand money over with a smile.</p>
  </div>
</section>

<footer class="abs footer">
  <div class="abs footer-brand"><span class="brand-dot"></span><span class="brand-name">Roam Pals</span></div>
  <div class="abs divider" style="left:208px"></div>
  <p class="abs footer-copy">Visit our website for more info and list of our favorite restaurants and places to stay!</p>
  <div class="abs footer-url">www.RoamPals.com</div>
  <div class="abs divider" style="left:812px"></div>
  <ul class="abs socials">
    <li>@roampals</li>
    <li>@roam_pals</li>
    <li>@roampals</li>
    <li>@roampals</li>
  </ul>
</footer>

</body>
</html>
```